A resource brochure for seniors and their families/Brookline Care Partners

As we age, the journey can come with unexpected challenges and obstacles. Brookline Care Partners is here to provide seniors and their families with a road map to navigate those challenges and insure the journey is as smooth as possible. We are a company that offers 'one stop shop' resources for seniors who need assistance with selling their home, need home care support or need to find suitable senior housing living choices and much more. We need this brochure to showcase a caring, clear and clear way for families or individuals, many who have just lost a spouse/parent, to find resources during a very difficult and confusing time in their life. The final design should communicate caring support, a call to action (call us!), and showcase a professional and knowledgeable team that will gently support and be a guide to families and individuals who are trying to make big life choices within the senior care arena.

Target Market(s)

A mature market- SENIORS (75+) and their families (adult children 50+) who typically are going through life changes such as losing a spouse or having to make a move from their home into a Retirement Community.

Industry/Entity Type

Group

Font styles to use
Serif
Script

Requirements
Must have
• Showcase a thoughtful and caring mentality- 'we will take care of you" in a professional and knowledgeable way. Please make it clear what the message is - we can assist with selling a home, bringing support and care into the home, find more appropriate housing as well as any resources or tools needed throughout the senior care spectrum of resources. Must have our name, logo, website and address and we need one panel to be laid out as a mailer- our address on top left. (Please see attached rough draft for address- thank you!) Also- please keep the testimonial, which is attached inclusive of additional verbiage.
Nice to have
• An attractive senior (female) on the cover of the brochure with a 'What's Next?" feel to engage people to open the collateral and relate to the story and purpose of what we do. Showcase what our services are- we are a company that guides families to and through much needed resources as it relates to aging and the ever-changing needs of an elderly person. We want to be the experts and trusted by our clients and the tough decisions that come along with aging. We offer our referral services at no cost to our clients.
Should not have
• Should not sound slick, 'sales-y' or too pushy- we are trying to build a relationship and not 'over sell'...we want to be a trusted resource guide and a helping hand.

```html
<!DOCTYPE html>
<html lang="en">
<head>
<meta charset="utf-8">
<title>Brookline Care Partners – Brochure</title>
<link href="https://fonts.googleapis.com/css2?family=Cinzel:wght@400;600&family=Roboto:ital,wght@0,300;0,400;1,300&family=Arimo:wght@400&display=swap" rel="stylesheet">
<style>
  :root{
    --navy:#464a6e;
    --navy-deep:#3b3f62;
    --gold:#f6b51e;
    --gold-rim:#d9a640;
    --paper:#ffffff;
    --panel-grey:#ececee;
    --ink:#1d1d1f;
    --text-grey:#333338;
    --backdrop:#e4e1dc;
  }
  *{box-sizing:border-box;margin:0;padding:0}
  html,body{width:1200px;height:943px;overflow:hidden;background:var(--backdrop)}
  .canvas{position:relative;width:1200px;height:943px;font-family:"Roboto",Arial,sans-serif}
  .brochure{position:absolute;left:35px;top:35px;width:1128px;height:870px;background:var(--paper);box-shadow:0 4px 14px rgba(0,0,0,.25)}
  .shapes{position:absolute;left:0;top:0;width:1200px;height:943px}
  .panel-middle-bg{position:absolute;left:408px;top:35px;width:378px;height:870px;background:linear-gradient(90deg,#f6f6f7,var(--panel-grey) 60%,#f4f4f5)}
  .panel-right-bg{position:absolute;left:786px;top:35px;width:377px;height:870px;background:linear-gradient(180deg,#fafafa,#ececee)}
  .t{position:absolute}
  .intro-copy{left:48px;top:578px;width:350px;font-family:"Arimo",Arial,sans-serif;font-size:17.2px;line-height:25.2px;color:var(--ink)}
  .top-bar{left:408px;top:35px;width:378px;height:63px;background:var(--navy);color:#fff;font-weight:300;font-size:28.5px;display:flex;align-items:center;justify-content:center}
  .headline{left:408px;top:122px;width:378px;text-align:center;font-family:"Cinzel",serif;font-weight:600;font-size:31px;color:var(--navy);letter-spacing:.5px}
  .lead{left:408px;top:182px;width:378px;text-align:center;font-style:italic;font-weight:300;font-size:24.5px;line-height:37px;color:#2a2a30}
  .services{left:452px;top:278px;width:330px;list-style:none;font-size:19.5px;font-weight:400;color:#2a2a30}
  .services li{margin-bottom:28px;line-height:37px}
  .services li::before{content:"• "}
  .services .wrap{padding-left:15px;display:block}
  .brand{display:flex;align-items:center;gap:10px;font-family:"Cinzel",serif;font-weight:600;color:var(--navy)}
  .brand-dot{width:22px;height:22px;border-radius:50%;background:var(--gold);flex:none}
  .brand-mid{left:408px;top:700px;width:378px;justify-content:center;font-size:22px}
  .brand-right{left:786px;top:760px;width:377px;justify-content:center;font-size:26px}
  .address{left:408px;top:790px;width:378px;text-align:center;font-size:17.5px;line-height:25px;color:#2a2a30}
  .contact-bar{left:408px;top:845px;width:378px;height:60px;background:var(--navy);color:#fff;font-size:19px;text-align:center;line-height:26px;padding-top:4px}
  .tag-bar{left:786px;top:845px;width:377px;height:60px;background:var(--navy);color:#fff;font-family:"Cinzel",serif;display:flex;align-items:center;justify-content:center;gap:7px;font-size:17px;letter-spacing:.5px}
  .tag-bar .big{font-size:23px}
  .badge-text{left:985px;top:500px;width:178px;text-align:center;font-family:"Cinzel",serif;font-size:34px;line-height:44px;color:#fff}
</style>
</head>
<body>
<div class="canvas">
  <div class="brochure"></div>
  <div class="panel-middle-bg"></div>
  <div class="panel-right-bg"></div>

  <svg class="shapes" viewBox="0 0 1200 943" xmlns="http://www.w3.org/2000/svg">
    <defs>
      <linearGradient id="coverPhoto" x1="0" y1="0" x2="0" y2="1">
        <stop offset="0" stop-color="#f4f1ec"/>
        <stop offset="0.5" stop-color="#e9dcc4"/>
        <stop offset="1" stop-color="#f7f7f7"/>
      </linearGradient>
      <linearGradient id="carePhoto" x1="0" y1="0" x2="1" y2="0">
        <stop offset="0" stop-color="#e8e2dc"/>
        <stop offset="0.6" stop-color="#cfd8e6"/>
        <stop offset="1" stop-color="#8fa6d6"/>
      </linearGradient>
    </defs>

    <!-- left panel photo and swoosh -->
    <path role="img" aria-label="Photo of a smiling senior woman with blonde hair in a white shirt" fill="url(#coverPhoto)"
          d="M35,35 H408 V285 C380,430 200,480 35,462 Z"/>
    <path fill="var(--gold)" d="M35,462 C200,480 380,430 408,285 V330 C390,450 220,505 35,500 Z"/>
    <path fill="var(--navy)" d="M35,500 C220,505 390,450 408,330 V395 C400,470 240,525 35,525 Z"/>

    <!-- right panel photo and swoosh -->
    <path role="img" aria-label="Photo of a nurse in blue scrubs talking with an elderly woman at her bedside" fill="url(#carePhoto)"
          d="M786,35 H1163 V468 L980,472 C860,470 800,400 786,260 Z"/>
    <path fill="var(--gold)" d="M786,260 C800,400 860,470 980,472 L1163,468 V490 L990,492 C870,490 800,430 786,300 Z"/>
    <path fill="var(--navy)" d="M786,300 C800,430 870,490 990,492 L1000,492 C940,505 900,515 960,522 C880,520 805,470 786,345 Z"/>

    <!-- what's next badge -->
    <path fill="var(--navy-deep)" stroke="var(--gold-rim)" stroke-width="7"
          d="M1000,482 H1166 V612 Q1100,628 1010,618 Q958,610 960,565 Q962,495 1000,482 Z"/>
  </svg>

  <p class="t intro-copy">Lorem Ipsum is simply dummy text of the printing and typesetting industry. Lorem Ipsum has been the industry's standard dummy text ever since the 1500s, when an unknown printer took a galley of type and scrambled it to make a type specimen book. It has survived not only five centuries, but also the leap into electronic typesetting, remaining essentially unchanged. It was popularised in the 1960s with the release of Letraset sheets containing Lorem Ipsum</p>

  <div class="t top-bar">Our company that offers</div>
  <h1 class="t headline">'ONE STOP SHOP'</h1>
  <p class="t lead">resources for seniors who<br>need assistance with</p>
  <ul class="t services">
    <li>selling their home,</li>
    <li>need home care support</li>
    <li>need to find suitable<span class="wrap">senior housing living choices</span></li>
    <li>much more</li>
  </ul>

  <div class="t brand brand-mid"><span class="brand-dot"></span>Brookline Care Partners</div>
  <p class="t address">4410 Harbor View Road, Suite 210<br>Maple Bay, WA. 98000</p>
  <div class="t contact-bar">Call us : (800) 555-0142<br>Email us : info@brooklinecare.com</div>

  <p class="t badge-text">'What's<br>Next?</p>
  <div class="t brand brand-right"><span class="brand-dot"></span>Brookline Care Partners</div>
  <div class="t tag-bar"><span>WE WILL</span><span class="big">TAKE CARE</span><span>OF YOU</span></div>
</div>
</body>
</html>
```